Hemp company needs website/online store

We are a startup hemp company and we need an online storefront designed. We are very open do design, but will include our logo to help. We make 100% hemp derived products like edibles, concentrates, vapes and THCA flower. Everything is grown locally, and all products are extracted and made in house.

Requirements
Nice to have
• I would like to highlight that we have Cannabis products that are hemp derived and 100% legal across the US. Also that all cannabis is locally grown and products are extracted and made in house and sent out for third party lab testing.

```html
<!DOCTYPE html>
<html lang="en">
<head>
<meta charset="utf-8">
<title>Sunny Field Hemp</title>
<link href="https://fonts.googleapis.com/css2?family=Baloo+2:wght@600;700;800&family=Poppins:ital,wght@0,400;0,500;0,600;0,700;1,400&display=swap" rel="stylesheet">
<style>
:root{
  --forest:#1d4418;
  --green:#3d7a2a;
  --text-green:#3a6a22;
  --lime:#9cb73a;
  --lime-soft:#cfdfa3;
  --grey-bg:#efefef;
  --footer-bg:#ebebeb;
  --ink:#333;
  --white:#fff;
}
*{margin:0;padding:0;box-sizing:border-box}
html,body{width:1200px;height:4107px;overflow:hidden}
body{position:relative;font-family:"Poppins",sans-serif;color:var(--ink);background:var(--white)}
.abs{position:absolute}
.heading{font-family:"Baloo 2",sans-serif;font-weight:700}

/* header + hero */
.hero{left:0;top:0;width:1200px;height:780px;background:linear-gradient(90deg,#16380f 0%,#1f4a18 40%,#3c6f2a 65%,#5f9440 100%)}
.hero-photo{left:640px;top:140px;width:560px;height:560px;background:radial-gradient(circle at 50% 50%,#6fa84a 0%,#3f7a2a 45%,rgba(31,74,24,0) 75%)}
.hero-wave{left:0;top:560px}
.search{left:127px;top:25px;width:271px;height:34px;border:2px solid #cfdc9e;border-radius:17px;color:#fff;font-size:13px;padding:7px 14px}
.search svg{position:absolute;right:12px;top:8px}
.nav{top:88px;font-size:15px;color:#fff;font-weight:500}
.nav a{color:#fff;text-decoration:none;margin-right:36px}
.nav a.active{color:var(--lime)}
.nav-rule{top:128px;height:2px;background:#b9cb79}
.icons{left:955px;top:26px;display:flex;gap:8px}
.icons span{width:34px;height:34px;border:2px solid #cfdc9e;border-radius:50%;display:flex;align-items:center;justify-content:center}
.icons span.cart{background:var(--lime);border-color:var(--lime)}
.brand{left:486px;top:40px;width:228px;text-align:center;color:var(--lime);font-family:"Baloo 2",sans-serif;font-weight:700;font-size:40px;line-height:1}
.brand .mark{display:block;width:46px;height:46px;border:3px solid var(--lime);margin:0 auto 6px}
.brand small{display:block;font-size:20px;letter-spacing:10px;margin-top:2px}
.hero-title{left:127px;top:262px;color:#fff;font-size:66px;line-height:1}
.hero-sub{left:127px;top:328px;color:#fff;font-size:48px;line-height:1}
.hero-sub em{font-style:normal;color:var(--lime)}
.btn{left:127px;top:403px;width:177px;height:50px;background:var(--lime);color:#fff;border-radius:4px;font-weight:600;font-size:16px;display:flex;align-items:center;justify-content:center}

/* prepare */
.prepare{left:0;top:773px;width:1200px;height:484px;background:linear-gradient(90deg,#c3d68a 0%,#dfeac0 50%,#eef3dd 60%)}
.prepare-photo{left:640px;top:773px;width:560px;height:484px;background:linear-gradient(135deg,#e8ece6 0%,#9fb88a 45%,#3f6e2c 80%,#d8b33a 100%)}
.prepare-top{left:0;top:760px}
.prepare-title{left:125px;top:875px;font-size:48px;color:var(--text-green)}
.step{left:127px;display:flex;align-items:center;gap:10px}
.step .ic{width:80px;height:80px;border-radius:50%;background:var(--green);display:flex;align-items:center;justify-content:center}
.step p{font-weight:600;font-size:19px;line-height:1.15;color:var(--text-green)}

/* products */
.products{left:0;top:1257px;width:1200px;height:480px;background:var(--grey-bg)}
.sec-title{left:0;width:1200px;text-align:center;font-size:50px;color:var(--text-green)}
.cat{top:1407px;width:213px;height:250px;background:#fff;border-radius:4px;box-shadow:0 2px 8px rgba(0,0,0,.12);overflow:hidden}
.cat .ph{height:192px}
.cat p{text-align:center;font-size:21px;font-weight:600;color:var(--green);padding-top:12px}

.item{top:1912px;width:213px;height:265px;background:#fff;box-shadow:0 2px 10px rgba(0,0,0,.1);border-radius:4px;text-align:center}
.item .ph{width:140px;height:120px;margin:20px auto 14px;border-radius:50%}
.item .name{font-size:17px;color:var(--green);font-weight:500}
.item .price{font-size:22px;color:var(--lime);font-weight:700}
.arrow{top:2023px}

/* banner */
.banner{left:0;top:2284px;width:1200px;height:362px;background:linear-gradient(90deg,#2d5f26 0%,#3d7a2e 50%,#2a5521 100%)}
.banner-photo{left:780px;top:2284px;width:420px;height:362px;background:radial-gradient(ellipse at 55% 50%,#7f9a4a 0%,#3d5a2a 45%,rgba(42,85,33,0) 78%)}
.banner-name{left:115px;top:2430px;color:#fff;font-family:"Baloo 2",sans-serif;font-weight:700;font-size:30px;display:flex;align-items:center;gap:10px}
.banner-name i{width:26px;height:26px;border:3px solid #fff;display:block}
.banner-text{left:340px;top:2405px;width:520px;text-align:center;color:#fff;font-size:50px;line-height:50px;letter-spacing:1px;font-weight:800}

/* about */
.about-frame{left:268px;top:2736px;width:805px;height:402px;border:3px solid var(--green)}
.about-photo{left:127px;top:2784px;width:322px;height:322px;border-radius:50%;background:linear-gradient(160deg,#dfe6e8 0%,#8aab5f 45%,#3e6b2a 100%)}
.about-title{left:512px;top:2795px;font-size:50px;color:var(--green)}
.about-copy{left:512px;top:2870px;width:505px;font-size:15px;line-height:25px;color:#555}

/* testimonial */
.quote{left:0;top:3226px;width:1200px;height:428px;background:var(--lime);color:#fff;text-align:center}
.quote .mark{font-family:"Baloo 2",sans-serif;font-size:150px;line-height:1;height:90px;margin-top:48px;font-weight:800}
.quote .txt{width:800px;margin:30px auto 0;font-style:italic;font-size:23px;line-height:28px}
.quote .who{font-size:25px;font-weight:600;margin-top:20px}
.quote .stars{font-size:22px;letter-spacing:4px}

/* footer */
.footer{left:0;top:3654px;width:1200px;height:453px;background:var(--footer-bg)}
.f-brand{left:126px;top:3790px;color:var(--green);font-family:"Baloo 2",sans-serif;font-weight:700;font-size:46px;line-height:1;display:flex;align-items:center;gap:10px}
.f-brand i{width:32px;height:32px;border:3px solid var(--green);display:block}
.f-head{top:3742px;font-size:21px;font-weight:600;color:var(--lime)}
.f-links{left:403px;top:3800px;font-size:15px;line-height:26px;color:#333;list-style:none}
.contact{left:567px;display:flex;gap:12px;align-items:center;font-size:14px;line-height:18px}
.contact .ic{width:40px;height:40px;border-radius:50%;background:var(--green);display:flex;align-items:center;justify-content:center;flex:none}
.news{left:831px;top:3804px;width:230px;font-size:14px;line-height:17px}
.email{left:832px;top:3856px;width:238px;height:46px;background:#fff;border-radius:23px;box-shadow:0 2px 6px rgba(0,0,0,.15);font-size:14px;padding:13px 18px}
.email span{position:absolute;right:6px;top:6px;width:34px;height:34px;border-radius:50%;background:var(--green);display:flex;align-items:center;justify-content:center}
.social{left:836px;top:3932px;display:flex;gap:8px}
.social i{width:37px;height:37px;border:2px solid #333;border-radius:50%;display:block}
.f-rule{left:115px;top:4029px;width:956px;height:1px;background:#aaa}
.copy{left:127px;top:4062px;font-size:15px}
.cards{left:830px;top:4063px;display:flex;gap:9px}
.cards i{width:34px;height:20px;border-radius:3px;display:block}
</style>
</head>
<body>

<section class="abs hero" aria-label="Hero"></section>
<div class="abs hero-photo" role="img" aria-label="Close-up photo of green hemp leaves"></div>
<svg class="abs hero-wave" width="1200" height="220" viewBox="0 0 1200 220" aria-hidden="true">
  <path d="M0,38 Q600,300 1200,50 L1200,220 L0,220Z" fill="#9cb73a"/>
  <path d="M0,38 Q600,340 1200,50 L1200,220 L0,220Z" fill="#fff"/>
</svg>

<div class="abs search">Search
  <svg width="14" height="14" viewBox="0 0 14 14"><circle cx="6" cy="6" r="4.5" stroke="#cfdc9e" stroke-width="2" fill="none"/><path d="M9.5 9.5L13 13" stroke="#cfdc9e" stroke-width="2"/></svg>
</div>
<div class="abs icons">
  <span><svg width="14" height="14" viewBox="0 0 14 14"><path d="M7 12L2 7a3 3 0 015-4 3 3 0 015 4z" fill="#cfdc9e"/></svg></span>
  <span><svg width="14" height="14" viewBox="0 0 14 14"><circle cx="7" cy="4.5" r="3" fill="#cfdc9e"/><path d="M1.5 13a5.5 5.5 0 0111 0z" fill="#cfdc9e"/></svg></span>
  <span class="cart"><svg width="16" height="14" viewBox="0 0 16 14"><path d="M1 1h3l2 8h8l1.5-6H5" stroke="#1d4418" stroke-width="1.8" fill="none"/><circle cx="7" cy="12" r="1.3" fill="#1d4418"/><circle cx="13" cy="12" r="1.3" fill="#1d4418"/></svg></span>
</div>
<nav class="abs nav" style="left:127px"><a class="active" href="#">Home</a><a href="#">About Us</a><a href="#">Our Products</a></nav>
<nav class="abs nav" style="left:776px"><a href="#">How to Prepare</a><a href="#">Blog</a><a href="#" style="margin-right:0">Contact</a></nav>
<div class="abs nav-rule" style="left:127px;width:345px"></div>
<div class="abs nav-rule" style="left:726px;width:348px"></div>
<div class="abs brand"><i class="mark"></i>Sunny Field<small>HEMP</small></div>

<h1 class="abs heading hero-title">Sunny Field</h1>
<h2 class="abs heading hero-sub"><em>Hemp</em> Products</h2>
<a class="abs btn">Our Products</a>

<section class="abs prepare" aria-label="How to prepare"></section>
<div class="abs prepare-photo" role="img" aria-label="Photo of a lab technician with a dropper and a flask of hemp oil beside a plant"></div>
<svg class="abs prepare-top" width="1200" height="110" viewBox="0 0 1200 110" aria-hidden="true">
  <path d="M0,0 H1200 V105 Q800,-40 0,100Z" fill="#fff"/>
</svg>
<h2 class="abs heading prepare-title">How to Prepare</h2>
<div class="abs step" style="top:953px"><span class="ic"><svg width="40" height="40" viewBox="0 0 40 40"><path d="M20 6v28M20 30L8 18M20 30l12-12M20 30L6 28M20 30l14-2" stroke="#fff" stroke-width="2.2" fill="none" stroke-linecap="round"/></svg></span><p>Cannabis is<br>locally grown</p></div>
<div class="abs step" style="top:1049px"><span class="ic"><svg width="40" height="40" viewBox="0 0 40 40"><path d="M6 20L20 8l14 12M10 17v15h20V17M17 32v-8h6v8" stroke="#fff" stroke-width="2.2" fill="none" stroke-linejoin="round"/></svg></span><p>Products are<br>made in house</p></div>
<div class="abs step" style="top:1135px"><span class="ic"><svg width="40" height="40" viewBox="0 0 40 40"><path d="M13 8h8M15 8v10l-6 12a2 2 0 002 3h12a2 2 0 002-3l-6-12V8M26 12v18a3 3 0 006 0V12z" stroke="#fff" stroke-width="2.2" fill="none" stroke-linejoin="round"/></svg></span><p>Sent out for third<br>party lab testing</p></div>

<section class="abs products" aria-label="Our products"></section>
<h2 class="abs heading sec-title" style="top:1305px">Our Products</h2>
<div class="abs cat" style="left:127px"><div class="ph" role="img" aria-label="Photo of blue hemp gummies with a leaf" style="background:linear-gradient(135deg,#6c8a4a,#4a6ea0 60%,#7a5a40)"></div><p>edibles</p></div>
<div class="abs cat" style="left:370px"><div class="ph" role="img" aria-label="Photo of amber concentrate in a jar" style="background:linear-gradient(135deg,#3a2a1a,#c98a2a 50%,#5a3a1a)"></div><p>concentrates</p></div>
<div class="abs cat" style="left:614px"><div class="ph" role="img" aria-label="Photo of vape cartridges on buds" style="background:linear-gradient(135deg,#7d8a4f,#d8d8c8 50%,#b0953a)"></div><p>vapes</p></div>
<div class="abs cat" style="left:856px"><div class="ph" role="img" aria-label="Photo of a flower bud held in a hand" style="background:linear-gradient(135deg,#dfe2e0,#6c7d3f 50%,#d8b8a8)"></div><p>THCA flower</p></div>

<h2 class="abs heading sec-title" style="top:1808px">Latest Products</h2>
<svg class="abs arrow" style="left:86px" width="14" height="22" viewBox="0 0 14 22"><path d="M11 2L3 11l8 9" stroke="#333" stroke-width="2.4" fill="none"/></svg>
<svg class="abs arrow" style="left:1098px" width="14" height="22" viewBox="0 0 14 22"><path d="M3 2l8 9-8 9" stroke="#333" stroke-width="2.4" fill="none"/></svg>
<div class="abs item" style="left:127px"><div class="ph" role="img" aria-label="Photo of a hemp flower bud" style="background:radial-gradient(#9aaa7a,#fff 72%)"></div><p class="name">Product Name</p><p class="price">$29.00</p></div>
<div class="abs item" style="left:371px"><div class="ph" role="img" aria-label="Photo of gummy bears with a leaf" style="background:radial-gradient(#f0a030,#fff 72%)"></div><p class="name">Product Name</p><p class="price">$29.00</p></div>
<div class="abs item" style="left:615px"><div class="ph" role="img" aria-label="Photo of amber shatter pieces" style="background:radial-gradient(#e0a028,#fff 72%)"></div><p class="name">Product Name</p><p class="price">$29.00</p></div>
<div class="abs item" style="left:859px"><div class="ph" role="img" aria-label="Photo of a tincture bottle and buds" style="background:radial-gradient(#8a5a2a,#fff 72%)"></div><p class="name">Product Name</p><p class="price">$29.00</p></div>

<section class="abs banner" aria-label="Hemp derived statement"></section>
<div class="abs banner-photo" role="img" aria-label="Photo of hemp buds in a metal grinder"></div>
<div class="abs banner-name"><i></i>Sunny Field</div>
<p class="abs heading banner-text">WE MAKE 100% HEMP DERIVED PRODUCTS</p>

<div class="abs about-frame"></div>
<div class="abs about-photo" role="img" aria-label="Photo of a farmer in a straw hat tending hemp plants in a field"></div>
<h2 class="abs heading about-title">About Us</h2>
<p class="abs about-copy">Lorem ipsum dolor sit amet, consectetur adipiscing elit, sed do eiusmod tempor incididunt ut labore et dolore magna aliqua. Quis ipsum suspendisse ultrices gravida. Risus commodo vive rra maecenas accumsan lacus vel facilisis. Lorem ipsum dolor sit amet, consectetur adipiscing elit, sed do eiusmod tempor incididunt ut labore et dolore magna aliqua. Quis ipsum suspendisse ultrices gravida.</p>

<section class="abs quote" aria-label="Testimonial">
  <div class="mark">&rdquo;</div>
  <p class="txt">Sed ut perspiciatis unde omnis iste natus error sit voluptatem accusa ntium doloremque audantium, totam rem aperiam, eaque ipsa quae ab illo inventore veritatis et quasi architecto beatae vitae dicta sunt explicabomo enim ipsam voluptatem quia</p>
  <p class="who">Mara Lindqvist</p>
  <p class="stars">★★★★★</p>
</section>
<svg class="abs" style="left:50px;top:3366px" width="28" height="52" viewBox="0 0 28 52"><path d="M25 3L4 26l21 23" stroke="#fff" stroke-width="4" fill="none"/></svg>
<svg class="abs" style="left:1094px;top:3366px" width="28" height="52" viewBox="0 0 28 52"><path d="M3 3l21 23L3 49" stroke="#fff" stroke-width="4" fill="none"/></svg>

<footer class="abs footer"></footer>
<div class="abs f-brand"><i></i>Sunny Field</div>
<h3 class="abs f-head" style="left:403px">Links</h3>
<ul class="abs f-links"><li>Home</li><li>About</li><li>Shop</li><li>Products</li><li>My Account</li><li>Shipping</li><li>FAQ's</li></ul>
<h3 class="abs f-head" style="left:567px">Contact Us</h3>
<div class="abs contact" style="top:3796px"><span class="ic"><svg width="16" height="20" viewBox="0 0 16 20"><path d="M8 19s6-7 6-11A6 6 0 002 8c0 4 6 11 6 11z" fill="#fff"/><circle cx="8" cy="8" r="2.2" fill="#3d7a2a"/></svg></span><span>Location Name<br>Sample Road 12,<br>Oregon 0000</span></div>
<div class="abs contact" style="top:3871px"><span class="ic"><svg width="18" height="18" viewBox="0 0 18 18"><path d="M4 1l3 4-2 2a10 10 0 006 6l2-2 4 3-2 3C8 17 1 10 1 3z" fill="#fff"/></svg></span><span>Phone:555.010.0199</span></div>
<div class="abs contact" style="top:3924px"><span class="ic"><svg width="18" height="14" viewBox="0 0 18 14"><rect width="18" height="14" rx="2" fill="#fff"/><path d="M1 2l8 6 8-6" stroke="#3d7a2a" stroke-width="1.6" fill="none"/></svg></span><span>hello@sunnyfield.example</span></div>
<h3 class="abs f-head" style="left:832px">Newsletter Sign up</h3>
<p class="abs news">Lorem ipsum dolor sit amelor conse ctet ur adipisclor.</p>
<div class="abs email">Email<span><svg width="16" height="14" viewBox="0 0 16 14"><path d="M1 7h13M9 2l5 5-5 5" stroke="#fff" stroke-width="2" fill="none"/></svg></span></div>
<div class="abs social"><i></i><i></i><i></i><i></i></div>
<div class="abs f-rule"></div>
<p class="abs copy">© 2024 All Rights Reserved.Terms &amp; Conditions Privacy Policy</p>
<div class="abs cards"><i style="background:#3b5aa0"></i><i style="background:#d8d8e6"></i><i style="background:#222"></i><i style="background:#e6e6ee"></i><i style="background:#4a8ac8"></i><i style="background:#e8c040"></i></div>

</body>
</html>
```